Sign listing benefits of Wash and Fold Service

Sign 48 inches wide and 24 inches height to showcase service listed above.
Benefits include:
Saves Money
Saves Time
Convenient
Stain Treatment

Looking for something colorful (Blue and white are our business colors) the look of a laundromat business.

```html
<!DOCTYPE html>
<html lang="en">
<head>
<meta charset="utf-8">
<title>Wash and Fold Service Sign</title>
<link href="https://fonts.googleapis.com/css2?family=Montserrat:wght@700;800;900&family=Pacifico&display=swap" rel="stylesheet">
<style>
  :root {
    --page-bg: #eef0f3;
    --navy-deep: #0b2a7e;
    --navy-mid: #0a55a6;
    --cyan-glow: #05a4cf;
    --aqua-light: #c8fdfd;
    --aqua-mid: #dcfbfc;
    --aqua-line: #12b8f0;
    --text-navy: #0d2779;
    --white: #ffffff;
    --orange: #ff6a00;
    --orange-light: #f7a21b;
    --basket-tone: #b88757;
    --towel-tone: #8fc7c9;
    --steel-light: #e7e8ea;
    --steel-dark: #9a9ca0;
  }
  * { box-sizing: border-box; margin: 0; padding: 0; }
  html, body {
    width: 1200px; height: 1200px; overflow: hidden;
    background: var(--page-bg);
  }
  .sign {
    position: absolute; left: 40px; top: 320px;
    width: 1120px; height: 560px; overflow: hidden;
    background: radial-gradient(ellipse 55% 70% at 55% 68%, var(--cyan-glow) 0%, var(--navy-mid) 50%, var(--navy-deep) 100%);
  }
  .sign-wave { position: absolute; left: 0; top: 0; width: 1120px; height: 560px; }
  .headline {
    position: absolute; left: 0; right: 0; top: 52px;
    text-align: center; color: var(--white);
    font-family: "Montserrat", sans-serif; font-weight: 900;
    font-size: 104px; line-height: 1; letter-spacing: 1px;
    text-shadow: 0 6px 18px rgba(0, 30, 90, 0.45);
  }
  .headline-script {
    position: absolute; left: 0; right: 0; top: 130px;
    text-align: center; color: var(--white);
    font-family: "Pacifico", cursive; font-size: 118px; line-height: 1.3;
    text-shadow: 0 6px 18px rgba(0, 30, 90, 0.45);
  }
  .benefits-label {
    position: absolute; left: 257px; top: 327px; width: 358px; height: 64px;
    border-radius: 32px; border: 3px solid var(--white);
    background: linear-gradient(90deg, var(--orange) 0%, var(--orange-light) 50%, var(--orange) 100%);
    color: var(--white); font-family: "Montserrat", sans-serif; font-weight: 800;
    font-size: 29px; display: flex; align-items: center; justify-content: center;
    box-shadow: 0 4px 10px rgba(0, 40, 100, 0.25);
  }
  .benefit-list { list-style: none; }
  .benefit {
    position: absolute; display: flex; align-items: center; gap: 14px;
    color: var(--text-navy); font-family: "Montserrat", sans-serif;
    font-weight: 800; font-size: 30px; line-height: 1;
  }
  .benefit svg { width: 34px; height: 34px; flex: none; }
  .photo-basket {
    position: absolute; left: 0; top: 287px; width: 244px; height: 255px;
    border-radius: 12px 40px 30px 0;
    background: linear-gradient(180deg, #d9c8b0 0%, var(--towel-tone) 40%, var(--basket-tone) 65%, #8a5d34 100%);
  }
  .photo-washer {
    position: absolute; left: 899px; top: 162px; width: 221px; height: 380px;
    background: linear-gradient(160deg, var(--steel-light) 0%, #c9cacc 55%, var(--steel-dark) 100%);
  }
</style>
</head>
<body>
  <main class="sign">
    <svg class="sign-wave" viewBox="0 0 1120 560" aria-hidden="true">
      <path d="M0 370 C 220 360, 300 330, 460 352 C 620 374, 760 400, 1120 404 L1120 560 L0 560 Z" fill="var(--aqua-line)"/>
      <path d="M0 376 C 220 366, 300 340, 460 362 C 620 384, 760 410, 1120 414 L1120 560 L0 560 Z" fill="var(--aqua-mid)"/>
      <rect x="0" y="520" width="1120" height="40" fill="var(--aqua-light)"/>
    </svg>

    <h1 class="headline">WASH AND FOLD</h1>
    <p class="headline-script">Service</p>

    <div class="benefits-label">Benefits include:</div>

    <ul class="benefit-list">
      <li class="benefit" style="left:256px; top:418px;">
        <svg viewBox="0 0 34 34"><circle cx="17" cy="17" r="16" fill="var(--orange)"/><circle cx="17" cy="17" r="12" fill="var(--orange-light)"/><path d="M10.5 17.5 L15 22 L23.5 12.5" fill="none" stroke="var(--white)" stroke-width="3.5" stroke-linecap="round" stroke-linejoin="round"/></svg>
        Saves Money
      </li>
      <li class="benefit" style="left:256px; top:471px;">
        <svg viewBox="0 0 34 34"><circle cx="17" cy="17" r="16" fill="var(--orange)"/><circle cx="17" cy="17" r="12" fill="var(--orange-light)"/><path d="M10.5 17.5 L15 22 L23.5 12.5" fill="none" stroke="var(--white)" stroke-width="3.5" stroke-linecap="round" stroke-linejoin="round"/></svg>
        Saves Time
      </li>
      <li class="benefit" style="left:543px; top:421px;">
        <svg viewBox="0 0 34 34"><circle cx="17" cy="17" r="16" fill="var(--orange)"/><circle cx="17" cy="17" r="12" fill="var(--orange-light)"/><path d="M10.5 17.5 L15 22 L23.5 12.5" fill="none" stroke="var(--white)" stroke-width="3.5" stroke-linecap="round" stroke-linejoin="round"/></svg>
        Convenient
      </li>
      <li class="benefit" style="left:543px; top:471px;">
        <svg viewBox="0 0 34 34"><circle cx="17" cy="17" r="16" fill="var(--orange)"/><circle cx="17" cy="17" r="12" fill="var(--orange-light)"/><path d="M10.5 17.5 L15 22 L23.5 12.5" fill="none" stroke="var(--white)" stroke-width="3.5" stroke-linecap="round" stroke-linejoin="round"/></svg>
        Stain Treatment
      </li>
    </ul>

    <div class="photo-basket" role="img" aria-label="Photo of folded towels in a wicker laundry basket"></div>
    <div class="photo-washer" role="img" aria-label="Photo of a silver front-loading washing machine"></div>
  </main>
</body>
</html>
```